Oven Cleaning Business owner needs business card design

Hi there,
Would like for a business card to be designed for myself, the owner of a professional oven cleaning business on the Sunshine Coast.
Would like it to look sleek, and modern-ish. Bit creative is encouraged too.
Include following:
Name/title: Corin Haldegaard, Owner
Phone number: 1300 482 936
Email: info@glowrangeco.com.au
Website: www.glowrangeco.com.au

```html
<!DOCTYPE html>
<html lang="en">
<head>
<meta charset="utf-8">
<title>Glow Range Co — Business Card</title>
<link href="https://fonts.googleapis.com/css2?family=Josefin+Sans:wght@300;400;600&display=swap" rel="stylesheet">
<style>
  :root {
    --teal: #4dbdc6;
    --ink: #0b0b0b;
    --paper: #f4f4f4;
    --backdrop: #6b6b6b;
    --muted: #2a2a2a;
  }
  * { box-sizing: border-box; margin: 0; padding: 0; }
  html, body { width: 1200px; height: 900px; overflow: hidden; }
  body {
    background: var(--backdrop);
    font-family: "Josefin Sans", sans-serif;
    position: relative;
  }
  .card {
    position: absolute;
    top: 140px;
    width: 340px;
    height: 620px;
    background: var(--paper);
    overflow: hidden;
    box-shadow: 0 18px 40px rgba(0,0,0,0.35);
  }
  .card--front { left: 170px; }
  .card--back { left: 690px; }
  .card__shapes { position: absolute; inset: 0; width: 100%; height: 100%; }

  .brand {
    position: absolute;
    display: flex;
    align-items: center;
    gap: 10px;
    font-weight: 600;
    letter-spacing: 1px;
    white-space: nowrap;
  }
  .brand__dot { border-radius: 50%; background: var(--teal); flex: none; }
  .card--front .brand { top: 120px; left: 30px; font-size: 30px; color: #ffffff; }
  .card--front .brand__dot { width: 18px; height: 18px; }
  .card--back .brand { top: 380px; left: 0; width: 100%; justify-content: center; font-size: 34px; color: var(--ink); }
  .card--back .brand__dot { width: 20px; height: 20px; }

  .person { position: absolute; top: 372px; right: 30px; text-align: right; }
  .person__name { font-size: 22px; font-weight: 400; color: var(--ink); letter-spacing: -0.5px; text-transform: uppercase; white-space: nowrap; }
  .person__role { font-size: 18px; font-weight: 300; color: var(--teal); margin-top: 4px; }

  .contact { position: absolute; top: 440px; right: 24px; list-style: none; }
  .contact__item {
    display: flex; align-items: center; justify-content: flex-end; gap: 8px;
    font-size: 15px; font-weight: 300; color: var(--muted); margin-bottom: 6px;
    white-space: nowrap;
  }
  .contact__icon { width: 14px; height: 14px; flex: none; }

  .back__web {
    position: absolute; top: 128px; right: 22px;
    font-size: 14px; font-weight: 300; letter-spacing: 2px; color: #ffffff;
    white-space: nowrap;
  }
  .back__web span { color: var(--teal); }
</style>
</head>
<body>

<section class="card card--front">
  <svg class="card__shapes" viewBox="0 0 340 620" preserveAspectRatio="none" aria-hidden="true">
    <polygon points="0,0 340,0 340,200 0,380" fill="var(--ink)"/>
    <polygon points="0,0 160,0 0,120" fill="var(--teal)"/>
    <polygon points="340,150 340,210 175,300" fill="var(--teal)"/>
    <path d="M0,588 C120,580 230,555 340,530 L340,620 L0,620 Z" fill="var(--teal)"/>
    <path d="M0,606 C130,600 240,578 340,555 L340,620 L0,620 Z" fill="var(--ink)"/>
  </svg>

  <div class="brand"><span class="brand__dot"></span>Glow Range Co</div>

  <div class="person">
    <p class="person__name">Corin Haldegaard</p>
    <p class="person__role">Owner</p>
  </div>

  <ul class="contact">
    <li class="contact__item">
      <svg class="contact__icon" viewBox="0 0 16 16"><path d="M2 6c0-2 3-3 6-3s6 1 6 3v1h-3V6H5v1H2z M4 8h8l2 6H2z" fill="var(--teal)"/></svg>
      1300 482 936
    </li>
    <li class="contact__item">
      <svg class="contact__icon" viewBox="0 0 16 16"><rect x="1" y="3" width="14" height="10" fill="var(--teal)"/><path d="M1 3l7 6 7-6" fill="none" stroke="#fff" stroke-width="1.2"/></svg>
      info@glowrangeco.com.au
    </li>
    <li class="contact__item">
      <svg class="contact__icon" viewBox="0 0 16 16"><circle cx="8" cy="8" r="6.5" fill="none" stroke="var(--teal)" stroke-width="1.5"/><path d="M1.5 8h13M8 1.5c-3 3-3 10 0 13M8 1.5c3 3 3 10 0 13" fill="none" stroke="var(--teal)" stroke-width="1"/></svg>
      www.glowrangeco.com.au
    </li>
  </ul>
</section>

<section class="card card--back">
  <svg class="card__shapes" viewBox="0 0 340 620" preserveAspectRatio="none" aria-hidden="true">
    <polygon points="120,0 340,0 340,80" fill="var(--teal)"/>
    <polygon points="0,0 120,0 340,80 340,230 0,160" fill="var(--ink)"/>
    <polygon points="0,160 150,190 0,270" fill="var(--teal)"/>
    <path d="M0,595 C120,588 240,565 340,535 L340,620 L0,620 Z" fill="var(--teal)"/>
    <path d="M0,610 C130,604 240,585 340,558 L340,620 L0,620 Z" fill="var(--ink)"/>
  </svg>

  <p class="back__web">www.<span>glowrangeco</span>.com.au</p>

  <div class="brand"><span class="brand__dot"></span>Glow Range Co</div>
</section>

</body>
</html>
```